Northbrook Vertebral Clinic of Weldon
Spine Surgeon
Professional
Grant Pellow, DO
Board Certified, Fellowship Trained, Reconstructive and Minimally Invasive Spine Surgery
5183 W. Tamsworth Rd., Suite 204
Weldon, TX 75149
unknown at this time
unknown
grantjpellow@mailvex.net
www.NorthbrookVertebralClinic.net
Board Certified, Orthopedic surgery
Fellowship Trained, Reconstructive and Minimally Invasive Spine Surgery
Clearly highlight that I am board certified and fellowship trained in spine surgery.
I am setting up a new office and do not have phone lines ect. I will be changing my email address to a business account
Treatment of:
Back and Neck Pain,
Arm and Leg Pain,
Degenerative Disc Disease of the Spine,
Spinal Stenosis,
Herniated Discs,
Scoliosis and Spinal Deformities,
Spinal Tumors and Infections,
Spinal Compression Fractures,
Worker's Compensation Injuries,
Motor Vehicle Injuries

```html
<!DOCTYPE html>
<html lang="en">
<head>
<meta charset="utf-8">
<title>Northbrook Vertebral Clinic of Weldon – Stationery</title>
<link href="https://fonts.googleapis.com/css2?family=Cinzel:wght@700&family=Open+Sans:wght@400;600;700&display=swap" rel="stylesheet">
<style>
  :root {
    --backdrop: #d6d8dc;
    --paper: #ffffff;
    --navy: #173a74;
    --blue: #2e5ea6;
    --blue-light: #4f7fc4;
    --ghost: #eceef3;
    --ink: #3a3d44;
    --muted: #7a7f89;
  }
  * { box-sizing: border-box; margin: 0; padding: 0; }
  html, body { width: 1200px; height: 871px; overflow: hidden; }
  body {
    background: var(--backdrop);
    font-family: "Open Sans", Arial, sans-serif;
    color: var(--ink);
    position: relative;
  }
  .sheet {
    position: absolute;
    background: var(--paper);
    box-shadow: 0 3px 10px rgba(0,0,0,.18);
    overflow: hidden;
  }
  .brand { display: flex; align-items: center; gap: 8px; }
  .brand-dot { border-radius: 50%; background: var(--navy); flex: none; }
  .brand-name {
    font-family: "Cinzel", Georgia, serif;
    font-weight: 700;
    color: var(--navy);
    text-transform: uppercase;
    line-height: 1.15;
  }
  .ghost-circle {
    position: absolute;
    border-radius: 50%;
    background: var(--ghost);
  }

  /* Envelope front */
  .envelope-front { left: 40px; top: 40px; width: 600px; height: 260px; }
  .envelope-front .brand { position: absolute; left: 26px; top: 24px; }
  .envelope-front .brand-dot { width: 22px; height: 22px; }
  .envelope-front .brand-name { font-size: 10px; }
  .envelope-front .ghost-circle { width: 300px; height: 300px; right: -70px; top: -70px; }
  .return-address {
    position: absolute; left: 26px; bottom: 22px;
    font-size: 7.5px; line-height: 1.5; color: var(--muted);
  }

  /* Envelope back */
  .envelope-back { left: 40px; top: 330px; width: 600px; height: 260px; }
  .envelope-back svg { position: absolute; inset: 0; }

  /* Business card back */
  .card-back {
    left: 40px; top: 640px; width: 290px; height: 166px;
    background: linear-gradient(135deg, var(--blue-light), var(--navy) 75%);
    color: #fff; padding: 16px 18px;
  }
  .card-back h3 { font-size: 9px; font-weight: 700; letter-spacing: .08em; text-transform: uppercase; margin-bottom: 6px; }
  .treatment-list { list-style: none; columns: 2; column-gap: 14px; font-size: 7.4px; line-height: 1.55; }

  /* Business card front */
  .card-front { left: 350px; top: 640px; width: 290px; height: 166px; }
  .card-front .band { position: absolute; right: 0; top: 0; bottom: 0; width: 10px; background: linear-gradient(var(--blue-light), var(--navy)); }
  .card-front .brand { position: absolute; left: 14px; top: 18px; }
  .card-front .brand-dot { width: 16px; height: 16px; }
  .card-front .brand-name { font-size: 7px; max-width: 110px; }
  .card-holder { position: absolute; right: 24px; top: 18px; text-align: right; width: 140px; }
  .card-holder .name { font-size: 11px; font-weight: 700; color: var(--navy); }
  .card-holder .credentials { font-size: 6.6px; line-height: 1.45; color: var(--muted); margin-top: 3px; }
  .card-contact { position: absolute; left: 14px; bottom: 14px; font-size: 6.8px; line-height: 1.55; color: var(--ink); }

  /* Letterhead */
  .letterhead { left: 680px; top: 40px; width: 480px; height: 621px; }
  .letterhead .ghost-circle { width: 300px; height: 300px; right: -90px; top: -60px; }
  .letterhead .brand { position: absolute; left: 40px; top: 50px; }
  .letterhead .brand-dot { width: 26px; height: 26px; }
  .letterhead .brand-name { font-size: 11px; }
  .letter-body {
    position: absolute; left: 40px; top: 150px; width: 330px;
    font-size: 7.6px; line-height: 1.6; color: var(--ink);
  }
  .letter-body p { margin-bottom: 10px; }
  .signature { margin-top: 24px; }
  .signature .signer { font-weight: 700; color: var(--navy); }
  .letter-footer {
    position: absolute; left: 40px; right: 40px; bottom: 26px;
    font-size: 6.8px; color: var(--muted); text-align: center;
  }
  .letter-band {
    position: absolute; left: 0; right: 0; bottom: 0; height: 12px;
    background: linear-gradient(90deg, var(--navy), var(--blue-light));
  }
</style>
</head>
<body>

  <section class="sheet envelope-front" aria-label="Envelope front">
    <div class="ghost-circle"></div>
    <div class="brand">
      <span class="brand-dot"></span>
      <span class="brand-name">Northbrook Vertebral<br>Clinic of Weldon</span>
    </div>
    <address class="return-address" style="font-style:normal">
      5183 W. Tamsworth Rd., Suite 204<br>
      Weldon, TX 75149
    </address>
  </section>

  <section class="sheet envelope-back" aria-label="Envelope back">
    <svg width="600" height="260" viewBox="0 0 600 260">
      <defs>
        <linearGradient id="flapFill" x1="0" y1="0" x2="0" y2="1">
          <stop offset="0" stop-color="#4f7fc4"/>
          <stop offset="1" stop-color="#173a74"/>
        </linearGradient>
      </defs>
      <polygon points="0,260 0,150 300,80 600,150 600,260" fill="url(#flapFill)"/>
      <polyline points="0,150 300,80 600,150" fill="none" stroke="#ffffff" stroke-opacity=".35" stroke-width="1"/>
      <circle cx="300" cy="92" r="16" fill="#ffffff"/>
      <circle cx="300" cy="92" r="10" fill="#173a74"/>
    </svg>
  </section>

  <section class="sheet card-back" aria-label="Business card back">
    <h3>Treatment of</h3>
    <ul class="treatment-list">
      <li>Back and Neck Pain</li>
      <li>Arm and Leg Pain</li>
      <li>Degenerative Disc Disease</li>
      <li>Spinal Stenosis</li>
      <li>Herniated Discs</li>
      <li>Scoliosis and Deformities</li>
      <li>Spinal Tumors and Infections</li>
      <li>Compression Fractures</li>
      <li>Worker's Compensation</li>
      <li>Motor Vehicle Injuries</li>
    </ul>
  </section>

  <section class="sheet card-front" aria-label="Business card front">
    <div class="band"></div>
    <div class="brand">
      <span class="brand-dot"></span>
      <span class="brand-name">Northbrook Vertebral Clinic of Weldon</span>
    </div>
    <div class="card-holder">
      <div class="name">Grant Pellow, DO</div>
      <div class="credentials">Board Certified, Orthopedic Surgery<br>Fellowship Trained, Reconstructive and Minimally Invasive Spine Surgery</div>
    </div>
    <div class="card-contact">
      5183 W. Tamsworth Rd., Suite 204<br>
      Weldon, TX 75149<br>
      grantjpellow@mailvex.net<br>
      www.NorthbrookVertebralClinic.net
    </div>
  </section>

  <section class="sheet letterhead" aria-label="Letterhead">
    <div class="ghost-circle"></div>
    <div class="brand">
      <span class="brand-dot"></span>
      <span class="brand-name">Northbrook Vertebral<br>Clinic of Weldon</span>
    </div>
    <div class="letter-body">
      <p>Date</p>
      <p>Recipient Name<br>Organization<br>Street Address<br>City, State ZIP</p>
      <p>Dear Colleague,</p>
      <p>Thank you for referring your patient to our practice. We have completed the initial evaluation and reviewed the imaging you provided with the referral.</p>
      <p>Our findings and the proposed plan of care are summarized in the enclosed report. Please contact our office with any questions about the next steps.</p>
      <p>We appreciate your trust and look forward to working together.</p>
      <div class="signature">
        <p>Sincerely,</p>
        <p class="signer">Grant Pellow, DO</p>
      </div>
    </div>
    <div class="letter-footer">5183 W. Tamsworth Rd., Suite 204 · Weldon, TX 75149 · grantjpellow@mailvex.net · www.NorthbrookVertebralClinic.net</div>
    <div class="letter-band"></div>
  </section>

</body>
</html>
```